Near future techno-thriller needs a mind blowing book cover design!

The Ash Tonic is the first in a trilogy of techno thrillers set in a very recognisable near future.

The world is changing. A mass market drug promised to boost intelligence. The world embraced it and soon everyone was a genius, but only for a while. The long term effects crippled the world societies. A select few experience much greater changes, becoming something more than human.

The book paints a Dustwalker like future, a society on the verge of collapse. The only two known posthumans are fighting an incomprehensible war against each other. Nils Carver, an old fashioned private investigator who is slowly losing his mental faculties as a result of the Drug, is tasked with capturing one of them.

This is a book that ask the question what we might become in the future, if our intellects expanded to the point where the boundaries of intellect no longer apply.

The winning designer will also be used for the second and third book in the series.

Author's name is "Jonas Beckholm"

MAIN CHARACTERS
Beyond the meta humans, there are two other main characters. This is the description from the book:

Nils Carver
Nils Carver is a private investigator in a world where they are no longer needed.

"ZipRoo studied the man next to him. Nils was asleep or at least it looked that way – his face always seemed set in a frown. Now that he was relaxed, half lying down in the car seat, he looked so old. ZipRoo knew he was thirty-six, but looked closer to fifty. His dark hair was turning grey. ZipRoo had seen photos of Nils in his mid-twenties. He had been quite handsome, making it hard to imagine what could have happened. Now he looked like an ageing movie star that had let himself go."

ZipRoo
ZipRoo is an operative for a posthuman interest group. He is an expert hacker and also a skilled stick fighter.

"A single streetlight created a cone of light in the centre of the playground, with everything else dimming into darkness. A young man was sitting on one of the swings, dangling his legs back and forth motionless. Like most people under 25, he had a completely integrated uPalo, and it was obvious he was doing something with it. From the occasional twitches in his fingers, Nils guessed he was playing a game. Nils approached him slowly, wondering if he’d come to the right place. As he got closer, he no longer had any doubts. The boy was of Asian descent and the spitting image of his father. He wore baggy pants and a black hoodie with a swirling pattern emanating from the chest. Expensive clothes designed to imitate what actual street kids wore. Nils hated the pretence.
As the more integrated systems almost completely disconnected you from what was going on around you, the uPalo allowed greetings that interrupted the current activity. Nils never had much time for such niceties. He walked up to the pretend gangster and tapped him on the forehead. The young man jolted backwards, tangled up in the swing and fell in a heap."

PROBABILITY MATRIX
One of the core concepts in the book is the idea of a probability matrix available to the posthumans. A mind map of decisions and probabilities. This concept would be interesting to see as the basis for the cover, or maybe the background, with a figure (either a posthuman or the private investigator) in the foreground. Here is a description from the book:

“Is this death?” Nils thought, his mind suspended in darkness.
A single light far away caught his attention. Was this the tunnel of light so common in near-death experiences? He focused on the light and willed himself to move towards it.
Nothing happened. He remained where he was as another light and then another appeared. At first they seemed random, but as they multiplied, thin strands of light connected them until what looked like a major city seen from above at night spread out below him.
It reminded him of the mind maps he could see when he was on the Drug, except much more complex. He no longer tried to move. He knew he was the centre of this space - everything else would move. He willed the map to take him to the beginning, that solitary spot he had first seen.
The dot represented his birth. All light surrounding him represented actions or decisions affecting him. Lines of varying colours and intensity led from this single dot to others, representing the probability.
He wanted to remain here to explore, but a distant pulsating light drew his attention. He travelled forward to now and studied the end of his life. To his surprise it didn’t end. From the current time there was a decision point with only a ten percent likelihood of death. The outgoing lines suggested many options. One in particular interested him as it had a high probability and included a line that seemed to depart from the matrix altogether. He followed it and a new matrix opened. This time the nodes were no longer decision points in his life. They were codes that translated to locations, people and devices as he studied them. It was a network diagram based on what he could access….

POSTHUMANS
Another core concept is the postHumans. They are people who has had their minds enhanced by the drug, but this is just the starting point. In the book one of the postHumans become a distributed mind, across multiple bodies. Another starts reconfiguring their body. Below are two sections from the book detailing this:

"Marva had made a remarkable recovery. Her skin had regenerated, shedding the old burnt one like sunburnt skin. The new skin was harder, more akin to a reptile’s, which made even taking blood samples difficult. Not that he knew what to do with them any longer, anyway. Most of her bodily processes had changed. She was still human, but only in the same sense that a Velo Prime car was a car. He suspected this was not a direct result of CortaVyn, but only a follow-on effect. The Drug had opened the door, but Marva was the architect behind the modifications, whether consciously or unconsciously. She had been killed, but managed to keep her body in a suspended state until the base functions could repair themselves and harden her body for any future attacks."

"My subconscious had begun a reconfiguration of what I was – a body to match the intellect it housed. It hadn’t even occurred to me until now that I could examine my body and its automatic processes in much the same as I could examine anything else.
What a marvelous machine it is, and yet so flawed.
It took only a cursory examination to question the possible involvement of a creator in its design. The mystery – if there was one – was how we had progressed this far at all. The spine was a prime example. It was an amazing construction for movement, but was obviously not for walking upright. Mine was reinforced, limiting movement somewhat. This was an understandable trade-off. Most of my physical enhancements, I discovered, were to better protect the brain and basic movement whilst limiting agility somewhat.
As I studied the different layers of the body, I found adjustments everywhere.
My metabolism had changed. I was now a hybrid with an organ specifically designed to store energy to feed my ever-increasing mind. Instead of allowing high-energy food such as sugars to flood my system, it stored them like a battery and released them as needed.
I had already seen the difference in analytics and critical thinking. The brain is an amazing organ, but to deal with the constant barrage of data and make sense of it, it filters, fills in the blanks and makes assumptions. My brain no longer did this. Instead it processed all information, made all the necessary connections and fed the result into the probability matrix.
The most surprising changes I found were in the building blocks of who I was. A completely new process was reprogramming my genome using designed viruses as the tool. A new organ created viruses and released them into the body. It changed the cell by infecting it, reprogramming all the cells in my body continuously. It was correcting deficiencies in my DNA."

Target Market(s)

From a cover perspective the book needs to capture readers who like near future sci-fi and techno thrillers. Here are some examples that have the right idea, but maybe slightly cheap looking approach:

http://www.brellashop.example/The-Quiet-Vessel-Lattice-Cycle-ebook/dp/Q47R2MXZTA/ref=pd_sim_351_2?ie=UTF8&refRID=5K2PQ8WZ7TLM4HNC3VR9

http://www.brellashop.example/ascent-Heron-Meridian-Book-ebook/dp/Q39KD7PLWE/ref=pd_sim_351_2?ie=UTF8&refRID=6Z8XQBN3MPRTWC5YHL04

Here is another that has similar themes:

http://www.brellashop.example/Quorra-The-Cycle-Book-ebook/dp/Q52WJ8HRVU/ref=pd_sim_351_2?ie=UTF8&refRID=3PLM7QKD2GNX9YTB4RS6

Industry/Entity Type

Drug

Requirements
Must have
• This is an eBook cover for a lumera. I also need a standard sized cover with spine and back cover. The back cover blurb:
• “You may wonder why I tell you this, but bear with me. I didn’t realize it then, but I had stumbled on something of enormous importance. Something that will redefine mankind. Something that could redefine you.”
• Gideon – postHuman
• The world is changing. A mass market drug promised to boost intelligence. The world embraced it and soon everyone was a genius, but only for a while. The long term effects crippled the world societies. A select few experience much greater changes, becoming something more than human.
• Nils Carver is hired by the very medical company that introduced the drug in the first place, to capture one of the posthumans. He finds himself part of a new world rising from the ashes of the old.
• The Ash Tonic is a scif-fi thriller set in a very recognisable near future.

```html
<!DOCTYPE html>
<html lang="en">
<head>
<meta charset="utf-8">
<title>The Ash Tonic — Cover Wrap</title>
<link href="https://fonts.googleapis.com/css2?family=Open+Sans:wght@300;400;700&family=Share+Tech+Mono&display=swap" rel="stylesheet">
<style>
  :root {
    --backdrop: #e4e4e4;
    --board: #1d1d1d;
    --board-edge: #262626;
    --signal-red: #e8231f;
    --signal-red-dim: rgba(232, 35, 31, 0.28);
    --paper-white: #f2f2f2;
    --muted-white: #cfcfcf;
  }
  * { margin: 0; padding: 0; box-sizing: border-box; }
  html, body {
    width: 1200px; height: 900px; overflow: hidden;
    background: var(--backdrop);
  }
  .cover-wrap {
    position: absolute; left: 170px; top: 150px;
    width: 860px; height: 600px;
    display: flex;
    box-shadow: 0 18px 40px rgba(0,0,0,0.25);
  }
  .panel {
    height: 100%;
    background: radial-gradient(ellipse at 40% 30%, var(--board-edge), var(--board) 70%);
    position: relative;
  }
  /* Back cover */
  .back-cover { width: 400px; padding: 56px 26px 0; }
  .back-quote {
    font-family: "Share Tech Mono", monospace;
    color: var(--signal-red);
    font-size: 14px; line-height: 1.2;
    text-align: center;
  }
  .rule {
    height: 2px; background: var(--signal-red);
    margin: 26px -26px 0 -26px;
  }
  .back-blurb {
    font-family: "Share Tech Mono", monospace;
    color: var(--paper-white);
    font-size: 13.5px; line-height: 1.2;
    text-align: center;
    margin-top: 48px;
  }
  .back-blurb + .back-blurb { margin-top: 24px; }
  .rule-lower { margin-top: 44px; }
  .back-tagline {
    font-family: "Open Sans", sans-serif; font-weight: 300;
    color: var(--muted-white);
    font-size: 16px; line-height: 1.3;
    margin-top: 16px; padding-left: 60px;
  }
  .back-tagline .title-mark { color: var(--signal-red); }
  /* Spine */
  .spine {
    width: 60px;
    display: flex; flex-direction: column; align-items: center;
    padding: 40px 0 26px;
    border-left: 1px solid #111; border-right: 1px solid #111;
  }
  .spine-title {
    writing-mode: vertical-rl;
    font-family: "Open Sans", sans-serif; font-weight: 300;
    color: var(--signal-red); font-size: 26px; letter-spacing: 4px;
  }
  .spine-emblem {
    width: 18px; height: 50px; margin: 18px 0;
    background: linear-gradient(180deg, var(--signal-red-dim), transparent);
  }
  .spine-author {
    margin-top: auto;
    writing-mode: vertical-rl;
    font-family: "Open Sans", sans-serif; font-weight: 700;
    color: var(--signal-red); font-size: 18px; letter-spacing: 1px;
    text-transform: uppercase;
  }
  /* Front cover */
  .front-cover { width: 400px; text-align: center; }
  .front-emblem {
    position: absolute; left: 100px; top: 60px;
    width: 180px; height: 180px;
    background: radial-gradient(circle at 50% 50%, var(--signal-red-dim), transparent 70%);
  }
  .front-title {
    position: absolute; left: 0; right: 0; top: 300px;
    font-family: "Open Sans", sans-serif; font-weight: 300;
    color: var(--signal-red);
    font-size: 56px; line-height: 1.12; letter-spacing: 18px;
    padding-left: 18px;
  }
  .front-author {
    position: absolute; left: 0; right: 0; bottom: 24px;
    font-family: "Open Sans", sans-serif; font-weight: 300;
    color: var(--signal-red);
    font-size: 24px; letter-spacing: 1px;
    text-transform: uppercase;
  }
</style>
</head>
<body>
  <main class="cover-wrap">
    <section class="panel back-cover">
      <p class="back-quote">You may wonder why I tell you this, but bear with me. I didn’t realize it then, but I had stumbled on something of enormous importance. Something that will redefine mankind. Something that could redefine you.</p>
      <div class="rule"></div>
      <p class="back-blurb">The world is changing. A mass market drug promised to boost intelligence. The world embraced it and soon everyone was a genius, but only for a while. The long term effects crippled the world societies. A select few experience much greater changes, becoming something more than human.</p>
      <p class="back-blurb">Nils Carver is hired by the very medical company that introduced the drug in the first place, to capture one of the posthumans. He finds himself part of a new world rising from the ashes of the old.</p>
      <div class="rule rule-lower"></div>
      <p class="back-tagline"><span class="title-mark">The Ash Tonic</span> is a scif-fi thriller set in a very recognisable near future.</p>
    </section>

    <section class="panel spine">
      <span class="spine-title">THE ASH TONIC</span>
      <div class="spine-emblem" role="img" aria-label="Small red outline capsule emblem"></div>
      <span class="spine-author">Jonas Beckholm</span>
    </section>

    <section class="panel front-cover">
      <div class="front-emblem" role="img" aria-label="Red line illustration of a tilted capsule pill"></div>
      <h1 class="front-title">THE<br>ASH<br>TONIC</h1>
      <p class="front-author">Jonas Beckholm</p>
    </section>
  </main>
</body>
</html>
```